New Custom Pizza Box Design Project For Independant Restaurant

We are looking for creative designs for our new custom printed pizza boxes. Designs should include the following:

-Our logo & company name
-A color scheme similar to our current logo
-Our physical and URL addresses & phone number (menu is attached)
-Ability to scale the design across several box sizes (10x10x2, 14x14x2, 18x13x2,
26x18x2)
- Any creative flair you think will make for the best design

Design can be on a white or kraft (tan) box.
Designs can be either two or three ink colors.

***Please note, designs must be able to be screen printed on boxes***
Updates

Reason: Still debating which to choose

Target Market(s)

Industry/Entity Type

Pizza Delivery

Font styles to use
Other font styles liked:
• Please use font similar to our logo text

Requirements
Must have
• -2 or 3 ink colors
• -company name, address, phone number, URL
• -company logo and colors
• -flexibility to use on different box sizes (10x10x2, 14x14x2, 18x13x2,
• 26x18x2)
• -utilize full printable area on boxes (including 2" dimension on box sides)
• ***Please note, designs must be able to be screen printed on boxes***
Should not have
• Design features with strong similarities to existing designs of other pizzerias

```html
<!DOCTYPE html>
<html lang="en">
<head>
<meta charset="utf-8">
<title>Marco's Henhouse &amp; Pizzeria — Pizza Box Dieline</title>
<link href="https://fonts.googleapis.com/css2?family=Oswald:wght@500&family=Open+Sans:wght@400;600&display=swap" rel="stylesheet">
<style>
  :root {
    --kraft: #c8b06b;
    --board-white: #ffffff;
    --brand-brown: #6b4a33;
    --brand-yellow: #f0b929;
    --ink-dark: #2e2218;
    --page-bg: #ece7df;
  }
  html, body {
    margin: 0;
    width: 1200px;
    height: 1200px;
    overflow: hidden;
    background: var(--page-bg);
  }
  .dieline { display: block; width: 1200px; height: 1200px; }
  .panel-kraft { fill: var(--kraft); }
  .panel-white { fill: var(--board-white); }
  .url-band { fill: var(--brand-brown); }
  .brand-name {
    font-family: "Oswald", sans-serif;
    font-weight: 500;
    fill: var(--brand-brown);
  }
  .badge-disc { fill: var(--brand-yellow); }
  .contact {
    font-family: "Open Sans", sans-serif;
    font-weight: 400;
    fill: var(--ink-dark);
    font-size: 10px;
  }
  .contact-strong { font-weight: 600; }
  .url-text {
    font-family: "Open Sans", sans-serif;
    font-size: 11px;
    letter-spacing: 5px;
    fill: #ffffff;
  }
</style>
</head>
<body>
<svg class="dieline" viewBox="0 0 1500 1500" xmlns="http://www.w3.org/2000/svg">
  <g class="lid">
    <rect class="panel-kraft" x="487" y="100" width="526" height="105"/>
    <rect class="panel-white" x="387" y="110" width="100" height="95" rx="14"/>
    <rect class="panel-white" x="1013" y="110" width="100" height="95" rx="14"/>
    <rect class="panel-kraft" x="381" y="205" width="106" height="528"/>
    <rect class="panel-kraft" x="1013" y="205" width="106" height="528"/>
    <rect class="panel-white" x="487" y="205" width="526" height="528"/>
    <rect class="panel-kraft" x="487" y="733" width="526" height="105"/>
    <rect class="panel-white" x="387" y="733" width="100" height="92" rx="14"/>
    <rect class="panel-white" x="1013" y="733" width="100" height="92" rx="14"/>

    <g class="lid-brand" transform="rotate(180 750 470)">
      <text class="brand-name" x="750" y="452" font-size="38" text-anchor="middle">MARCO'S HENHOUSE</text>
      <text class="brand-name" x="750" y="500" font-size="30" text-anchor="middle">&amp; PIZZERIA</text>
    </g>
  </g>

  <g class="front-wall">
    <rect class="panel-kraft" x="387" y="838" width="104" height="520"/>
    <rect class="panel-kraft" x="1010" y="838" width="104" height="520"/>
    <path class="panel-kraft" d="M491 1358 H1010 V1380 L1000 1398 H501 L491 1380 Z"/>

    <defs>
      <linearGradient id="hero-tones" x1="0" y1="0" x2="0" y2="1">
        <stop offset="0" stop-color="#f4f4f2"/>
        <stop offset="0.45" stop-color="#e9e6e1"/>
        <stop offset="0.7" stop-color="#d98a3a"/>
        <stop offset="1" stop-color="#c9552b"/>
      </linearGradient>
    </defs>
    <rect x="491" y="838" width="519" height="499" fill="url(#hero-tones)" role="img" aria-label="Photo of a pizza with olives, peppers and basil beside tomatoes, a yellow pepper and a bowl of salad, over a light sketched pizza-slice pattern"/>

    <g class="front-badge">
      <circle class="badge-disc" cx="600" cy="945" r="92"/>
      <text class="brand-name" x="600" y="925" font-size="26" text-anchor="middle">MARCO'S</text>
      <text class="brand-name" x="600" y="957" font-size="26" text-anchor="middle">HENHOUSE</text>
      <text class="brand-name" x="600" y="989" font-size="20" text-anchor="middle">&amp; PIZZERIA</text>
    </g>

    <rect class="url-band" x="491" y="1337" width="519" height="23"/>
    <text class="url-text" x="750" y="1352" text-anchor="middle">Log on : www.marcoshenhouse.com</text>

    <g class="side-contact-left" transform="translate(462 1002) rotate(90)">
      <text class="brand-name" x="0" y="10" font-size="11">MARCO'S HENHOUSE</text>
      <text class="brand-name" x="0" y="24" font-size="9">&amp; PIZZERIA</text>
      <text class="contact contact-strong" x="92" y="8">Call us : 555-014-2290</text>
      <text class="contact" x="92" y="20">Riverside Plaza</text>
      <text class="contact" x="92" y="32">1420 Elm Avenue</text>
      <text class="contact" x="92" y="44">Springfield, NY 10000</text>
    </g>

    <g class="side-contact-right" transform="translate(1036 1190) rotate(-90)">
      <text class="brand-name" x="0" y="22" font-size="11">MARCO'S HENHOUSE</text>
      <text class="brand-name" x="0" y="36" font-size="9">&amp; PIZZERIA</text>
      <text class="contact contact-strong" x="88" y="8">Call us : 555-014-2290</text>
      <text class="contact" x="88" y="20">Riverside Plaza</text>
      <text class="contact" x="88" y="32">1420 Elm Avenue</text>
      <text class="contact" x="88" y="44">Springfield, NY 10000</text>
    </g>
  </g>
</svg>
</body>
</html>
```